Postcard designed to acquire new customers

Need a postcard style AD to place in dentist offices and other professionals to promote our tax saving system. We will place these in dentists offices, orthodontist, optometrist, physiotherapist and all sorts of medical/dental offices. The card should highlight how they can save taxes by using our software. Our website has good information on it, and I'll include the advertising PDF that our software company produces. Our logo is a little out-dated and I've included the bonus of the winner re-making the logo so its better than it currently is.
Updates

I don't need to have any space allocated for a stamp and address. We are using this to place in offices and are for advertising purposes, not mailing. Thanks!

Reason: My apologies for not providing feedback yet, I've lost several days due to some illness and am finally back at work. I'll be going through designs today and would like the extra few days to work with many of you to create a great design. Thank you for your patience! Doyle

Reason: Again, my apologies for the delay. I will be in contact with designers this week. Thank you,

Target Market(s)

Small Business Owners in Canada

Industry/Entity Type

Health Insurance

Logo Text

Save Time, Save Money

Font styles to use
Other font styles liked:
• Easy to Read Font's

Colors

Designer to choose colors to be used in the design.

Requirements
Must have
• Must have a call to action on the postcard to sell the service. We need people to have their attention caught. A call to action could be, "You're spending too much on taxes! That's what they'll say if your business doesn't have a 789 Brookvale Outlay Plan..."
• See the PDF for other catch phrases or key information on what a Health Spending Account is. Many people don't know so I'd like to see 3-4 bullet points on the front of the postcard on what a health spending account is. See the attached PDF for that information and simplifying the information to short bullet points would be best. Here are my thoughts:
• Who should have a 789 Brookvale Outlay Plan?
• - Every business owner who is incorporated should have one.
• - Write off 100% of this QTB approved this method.
• - It is the most tax effective way to run dental, health, vision and other expenses through your company.
• - Easy to use APP for your phone, 2-day turnaround time for claims
• If you aren't using this, you're throwing tax dollars away!
• The back of the postcard would include 2 things. First, an example of the taxes you can save, and second - the different information they can send us so we can setup your account.
• First is the example of how this saves you money. Assuming a 38% personal tax rate. You will need to earn $1.62 of gross income, pay $0.62 of personal tax, which leaves you with $1.00 of after tax money to use for your personal expenses.
• The example of using a 789 Brookvale Outlay Plan, or doing nothing would need the following information.
• Comparison
• $5,000 of medical, dental, vision expenses
• Do Nothing 789 Brookvale Outlay Plan
• $8,100 – Total Cost $5,525 – Total Cost
• $3,100 – Income Tax $500 fee & $25 GST
• $5,000 – Money needed for medical, dental, vision, etc. $5,000 – Money needed for medical, dental, vision, etc.
• SAVINGS is $2,575
• Assuming a company incorporated in Alberta and a one time setup fee of $275 has not been included in the comparison.
• Information to send us to setup your account is:
• - Names and birth dates of you and your dependents
• - Contact information for you and your business (if different) Address, email, phone numbers
• - We will contact you about how to setup the app, your banking details and some other items.
• - Setup fee is a one-time payment of $275
Nice to have
• I'd like the front of the postcard to not be very busy with the background or graphics, etc. I want the call to action to be very obvious so they want to read the bullet points and look at the back of the postcard for more information.

```html
<!DOCTYPE html>
<html lang="en">
<head>
<meta charset="utf-8">
<title>789 Brookvale Outlay Plan – How it Works</title>
<link href="https://fonts.googleapis.com/css2?family=Montserrat:wght@600;700&family=Roboto:wght@400;500;700&display=swap" rel="stylesheet">
<style>
  :root {
    --teal-dark: #0d7b88;
    --teal: #13a6b9;
    --cyan: #3ec4e0;
    --heading: #1ba4ba;
    --paper: #f2f2f2;
    --ink: #1d1d1d;
    --white: #ffffff;
    --envelope: #ece3d4;
    --envelope-shade: #ddd1bd;
  }
  * { margin: 0; padding: 0; box-sizing: border-box; }
  html, body { width: 1200px; height: 776px; overflow: hidden; }
  body { font-family: "Roboto", Arial, sans-serif; color: var(--ink); background: var(--paper); }
  .postcard { position: relative; width: 1200px; height: 776px; background: var(--paper); overflow: hidden; }

  .top-band { position: absolute; left: 0; top: 0; width: 1200px; height: 41px; }

  .section-title {
    position: absolute; font-family: "Montserrat", Arial, sans-serif; font-weight: 700;
    font-size: 27px; color: var(--heading); letter-spacing: 0.2px;
  }
  .how-title { left: 83px; top: 91px; }
  .setup-title { left: 671px; top: 91px; }

  .intro {
    position: absolute; left: 84px; top: 150px; width: 467px;
    font-size: 17.4px; line-height: 21px; text-align: justify;
  }

  .compare-card {
    position: absolute; top: 272px; width: 222px; height: 279px;
    background: var(--teal); border-radius: 3px; color: var(--white);
  }
  .compare-card.with { left: 85px; }
  .compare-card.without { left: 329px; }
  .compare-icon { position: absolute; left: 92px; top: 14px; width: 38px; height: 38px; }
  .compare-name {
    position: absolute; top: 71px; left: 0; width: 100%; text-align: center;
    font-weight: 700; font-size: 15px; line-height: 20px;
  }
  .compare-body { position: absolute; left: 22px; top: 130px; font-size: 15.5px; line-height: 24px; }
  .compare-body .amount { padding-left: 17px; font-weight: 500; }
  .savings { position: absolute; left: 0; width: 100%; top: 223px; text-align: center; font-size: 18px; font-weight: 700; }
  .cost-table { position: absolute; left: 22px; top: 130px; font-size: 15.5px; line-height: 24px; border-collapse: collapse; }
  .cost-table td { padding: 0; vertical-align: top; }
  .cost-table td.value { padding-left: 14px; font-weight: 500; }
  .cost-table td.indent { padding-left: 14px; }

  .footnote {
    position: absolute; left: 84px; top: 589px; width: 467px;
    font-size: 17.4px; line-height: 21px; text-align: justify;
  }

  .info-card {
    position: absolute; left: 726px; top: 218px; width: 346px; height: 368px;
    background: var(--white); border-radius: 3px; box-shadow: 0 1px 3px rgba(0,0,0,0.06);
  }
  .envelope {
    position: absolute; left: 698px; top: 162px; width: 200px; height: 122px;
    background: linear-gradient(160deg, var(--envelope), var(--envelope-shade));
    transform: rotate(-12deg); border-radius: 2px;
  }
  .ribbon { position: absolute; left: 870px; top: 229px; width: 208px; height: 57px; }
  .ribbon-label {
    position: absolute; left: 886px; top: 236px; width: 180px; text-align: center;
    color: var(--white); font-weight: 700; font-size: 17px; line-height: 21px;
  }
  .info-list { position: absolute; left: 746px; top: 308px; width: 310px; list-style: none; }
  .info-list li { position: relative; padding-left 18px; padding-left: 18px; font-size: 15.2px; line-height: 18.5px; margin-bottom: 18px; }
  .info-list li svg { position: absolute; left: 0; top: 4px; width: 11px; height: 9px; }
  .info-list .sub { display: block; padding-left: 17px; }
  .info-note {
    position: absolute; left: 760px; top: 490px; width: 300px; text-align: center;
    font-size: 15.2px; line-height: 18.5px;
  }
  .fee-badge { position: absolute; left: 980px; top: 530px; width: 140px; height: 140px; }
  .fee-text {
    position: absolute; left: 980px; top: 571px; width: 140px; text-align: center;
    color: var(--white); font-weight: 500; font-size: 14px; line-height: 16px;
  }
  .fee-text strong { display: block; font-size: 19px; margin-top: 7px; font-weight: 700; }

  .footer { position: absolute; left: 0; top: 708px; width: 1200px; height: 68px; background: var(--teal-dark); }
  .brand {
    position: absolute; left: 56px; top: 22px; display: flex; align-items: center; gap: 10px;
    color: var(--white); font-family: "Roboto", Arial, sans-serif; font-weight: 700; font-size: 17px; letter-spacing: 0.5px;
  }
  .brand-mark { width: 20px; height: 20px; background: var(--cyan); }
  .contact {
    position: absolute; right: 27px; top: 24px; color: var(--white);
    font-size: 17.4px; font-weight: 500; letter-spacing: 0.3px; word-spacing: 1px;
  }
  .contact .sep { margin: 0 8px; }
</style>
</head>
<body>
<main class="postcard">
  <svg class="top-band" viewBox="0 0 1200 41" preserveAspectRatio="none" aria-hidden="true">
    <rect width="1200" height="41" fill="#0d7b88"/>
    <polygon points="380,0 1200,0 1200,41 620,41" fill="#3ec4e0"/>
    <polygon points="380,0 820,0 620,41" fill="#1fa7c0"/>
  </svg>

  <h2 class="section-title how-title">How it Works?</h2>
  <p class="intro">Assuming a 38% personal tax rate. You will need to earn $1.62 of gross income, pay $0.62 of personal tax, which leaves you with $1.00 of after tax money to use for your personal expenses.</p>

  <section class="compare-card with">
    <svg class="compare-icon" viewBox="0 0 38 38" aria-hidden="true">
      <circle cx="19" cy="19" r="17" fill="none" stroke="#fff" stroke-width="2.5"/>
      <polyline points="11,19.5 17,25 27,13" fill="none" stroke="#fff" stroke-width="2.8" stroke-linecap="round" stroke-linejoin="round"/>
    </svg>
    <h3 class="compare-name">w/ 789 Brookvale<br>Outlay Plan</h3>
    <div class="compare-body">
      Medical, dental, vision<br>expenses:<br><span class="amount">$5000</span>
    </div>
    <p class="savings">SAVINGS: $2,575</p>
  </section>

  <section class="compare-card without">
    <svg class="compare-icon" viewBox="0 0 38 38" aria-hidden="true">
      <circle cx="19" cy="19" r="17" fill="none" stroke="#fff" stroke-width="2.5"/>
      <path d="M13 13 L25 25 M25 13 L13 25" stroke="#fff" stroke-width="2.8" stroke-linecap="round"/>
    </svg>
    <h3 class="compare-name">w/o 789 Brookvale<br>Outlay Plan</h3>
    <table class="cost-table">
      <tr><td colspan="2">Medical, dental, vision</td></tr>
      <tr><td class="indent">expenses:</td><td class="value">$5000</td></tr>
      <tr><td>Income Tax:</td><td class="value">$500</td></tr>
      <tr><td>GST:</td><td class="value">$25</td></tr>
    </table>
  </section>

  <p class="footnote">* Assuming a company incorporated in Alberta and a one time setup fee of $275 has not been included in the comparison.</p>

  <h2 class="section-title setup-title">Setting Up Your Account:</h2>
  <div class="envelope" role="img" aria-label="Illustration of a cream paper envelope"></div>
  <div class="info-card"></div>
  <svg class="ribbon" viewBox="0 0 208 57" aria-hidden="true">
    <polygon points="0,0 208,0 194,28.5 208,57 0,57 10,28.5" fill="#13a6b9"/>
  </svg>
  <p class="ribbon-label">SEND US YOUR INFORMATION</p>

  <ul class="info-list">
    <li>
      <svg viewBox="0 0 11 9" aria-hidden="true"><polyline points="1,4.5 4,7.5 10,1" fill="none" stroke="#13a6b9" stroke-width="2"/></svg>
      Names and birth dates of you and your dependents
    </li>
    <li>
      <svg viewBox="0 0 11 9" aria-hidden="true"><polyline points="1,4.5 4,7.5 10,1" fill="none" stroke="#13a6b9" stroke-width="2"/></svg>
      Contact information for you and your business (if different)
      <span class="sub">Address</span>
      <span class="sub">E-mail</span>
      <span class="sub">Phone Numbers</span>
    </li>
  </ul>
  <p class="info-note">We will contact you about how to setup the app, your banking details and some other items.</p>

  <svg class="fee-badge" viewBox="0 0 140 140" aria-hidden="true">
    <g fill="#3ec4e0">
      <circle cx="70" cy="70" r="58"/>
      <circle cx="70" cy="14" r="14"/><circle cx="70" cy="126" r="14"/>
      <circle cx="14" cy="70" r="14"/><circle cx="126" cy="70" r="14"/>
      <circle cx="30.4" cy="30.4" r="14"/><circle cx="109.6" cy="30.4" r="14"/>
      <circle cx="30.4" cy="109.6" r="14"/><circle cx="109.6" cy="109.6" r="14"/>
      <circle cx="48.6" cy="18.3" r="14"/><circle cx="91.4" cy="18.3" r="14"/>
      <circle cx="48.6" cy="121.7" r="14"/><circle cx="91.4" cy="121.7" r="14"/>
      <circle cx="18.3" cy="48.6" r="14"/><circle cx="18.3" cy="91.4" r="14"/>
      <circle cx="121.7" cy="48.6" r="14"/><circle cx="121.7" cy="91.4" r="14"/>
    </g>
    <circle cx="70" cy="70" r="52" fill="none" stroke="#fff" stroke-width="2"/>
  </svg>
  <p class="fee-text">ONE-TIME<br>SET UP FEE<strong>$275</strong></p>

  <footer class="footer">
    <div class="brand"><span class="brand-mark"></span>789 BROOKVALE</div>
    <p class="contact">555 010 0199<span class="sep">|</span>HELLO@BROOKVALEPLAN.CA<span class="sep">|</span>WWW.BROOKVALEPLAN.CA</p>
  </footer>
</main>
</body>
</html>
```